Etikett für Rosé Wein
Zielgruppe
Wir sind ein Weingut das Weine im Premiumsegment produziert.
Wir haben vor einen neuen, hochwertigen Roséwein zu launchen. (Ca. 15 Euro Verkaufspreis)
DIe Flaschenform ist dabei an die Premiumweingüter aus der Provence angelehnt. (als Beispiel Silent Meadow als Datei dabei)
Der Wein wird ein Markenwein sein, das bedeutet der Weinname wir in der Vermarktung wichtiger sein als unser Weingutsname. Der Wein wird unter der Bezeichnung LUMARA vermarket werden.
Der Wein wird eine rose- goldende Kapsel erhalten(ähnlich Silent Meadow) - Datei unserer Kapsel anbei.
Folgende Bestandteile müssen am Etikett zu finden sein.
LUMARA
premium organic Rosé
2021(Jahrgang)
Kessel - Logo(nur die Grafik, nicht der Text Weingut Tobias Kessel der unter dem Logo steht)
Eventuell hätten wir noch gerne ein kleines Icon dabei, etwa eine Illustration eines Vogels oder zBsp. eines Blatt als Skelett oder ähnlich. Oder aber/auch das Logo der alpenländischen Erbkellereien könnte als Icon dienen(ebenfalls als Datei dabei)
Aufgabenstellung
Bei diesem Vorderseiten - Flaschenetikett ist uns eine hochwertige, aussagekräftige Etikette wichtig. Das Etikett muss leicht konisch sein, da die Flasche konisch ist. Die Glasfarbe der Flasche ist weiß durchsichtig, sodass die Farbe des Roseweines gut zur Geltung kommt.
Die max. Etikettenhöhe kann 90 mm betragen. Der Winkel der Flasche ist auf der technischen Zeichnun ersichtlich, von unten nach oben verlaufend, sprich im unteren Teil muss das Etikett schmäler sein als im oberen Bereich. Eine technische Zeichnung der Flasche ist als Datei angehängt.
Ebenso 1. Flaschenfoto einer Originalflache des Mitbewerbs(Fiorello), so wird unsere Flaschen ausssehen.

```html
<!DOCTYPE html>
<html lang="de">
<head>
<meta charset="utf-8">
<title>Lumara Rosé – Etikett</title>
<link rel="stylesheet" href="https://fonts.googleapis.com/css2?family=Montserrat:wght@500&family=Oswald:wght@200;300&family=Parisienne&family=Playfair+Display:wght@400&display=swap">
<style>
  :root {
    --bg-top: #ffe6e8;
    --bg-bottom: #fdb3b6;
    --label-fill: #ffffff;
    --label-border: #d9626f;
    --gold-light: #ecd6a0;
    --gold: #cfa35a;
    --gold-deep: #b98a3e;
    --plum: #5b3f7a;
    --rose-red: #c8102e;
    --coral: #d9626f;
  }
  * { margin: 0; padding: 0; box-sizing: border-box; }
  html, body { width: 900px; height: 1200px; overflow: hidden; }
  body {
    background: linear-gradient(180deg, var(--bg-top) 0%, var(--bg-bottom) 100%);
    position: relative;
  }
  .wine-label {
    position: absolute;
    left: 130px;
    top: 210px;
    width: 640px;
    height: 780px;
  }
  .wine-label__shape { position: absolute; inset: 0; width: 640px; height: 780px; }
  .wine-label__shape path { fill: var(--label-fill); stroke: var(--label-border); stroke-width: 8; }
  .centered {
    position: absolute;
    left: 0;
    width: 640px;
    text-align: center;
  }
  .estate-name {
    top: 70px;
    font-family: "Oswald", sans-serif;
    font-weight: 200;
    font-size: 52px;
    letter-spacing: 2px;
    color: var(--gold-light);
    line-height: 1;
  }
  .wine-name {
    top: 150px;
    font-family: "Parisienne", cursive;
    font-size: 170px;
    line-height: 1.1;
    background: linear-gradient(90deg, var(--gold-light) 0%, var(--gold-deep) 40%, var(--gold) 70%, var(--gold-light) 100%);
    -webkit-background-clip: text;
    background-clip: text;
    color: transparent;
  }
  .wine-quality {
    top: 372px;
    font-family: "Montserrat", sans-serif;
    font-weight: 500;
    font-size: 20px;
    letter-spacing: 2.5px;
    color: var(--plum);
  }
  .wine-type {
    top: 428px;
    font-family: "Playfair Display", serif;
    font-size: 62px;
    line-height: 1;
    color: var(--rose-red);
  }
  .divider {
    position: absolute;
    left: 180px;
    top: 505px;
    width: 275px;
    height: 1.5px;
    background: var(--coral);
  }
  .volume, .alcohol {
    position: absolute;
    top: 482px;
    font-family: "Oswald", sans-serif;
    font-weight: 300;
    font-size: 30px;
    line-height: 1;
    color: var(--coral);
  }
  .volume { left: 76px; }
  .alcohol { left: 478px; }
  .vintage {
    top: 522px;
    font-family: "Playfair Display", serif;
    font-size: 34px;
    line-height: 1;
    color: var(--plum);
  }
  .partner-badge {
    position: absolute;
    left: 279px;
    top: 600px;
    width: 80px;
    height: 80px;
    border-radius: 50%;
    border: 2px solid var(--plum);
  }
  .ornament {
    position: absolute;
    left: 250px;
    top: 712px;
    width: 140px;
    height: 36px;
    border-radius: 18px;
    background: linear-gradient(90deg, var(--gold-light), var(--gold), var(--gold-light));
  }
</style>
</head>
<body>
  <div class="wine-label">
    <svg class="wine-label__shape" viewBox="0 0 640 780" aria-hidden="true">
      <path d="M8,310 C8,140 160,10 320,10 C480,10 632,140 632,310 L602,716 Q598,770 544,770 L96,770 Q42,770 38,716 Z"/>
    </svg>
    <div class="centered estate-name">KESSEL</div>
    <div class="centered wine-name">Lumara</div>
    <div class="centered wine-quality">PREMIUM ORGANIC</div>
    <div class="centered wine-type">ROSÉ</div>
    <div class="volume">℮ 0.75L</div>
    <div class="divider"></div>
    <div class="alcohol">VOL.11,4%</div>
    <div class="centered vintage">2021</div>
    <div class="partner-badge" role="img" aria-label="Siegel der Partnervereinigung"></div>
    <div class="ornament" role="img" aria-label="Goldenes Blattornament"></div>
  </div>
</body>
</html>
```